Business card design needed

New company based in Brisbane, Australia. Brindle Systems. The business is focused on the delivery of network architecture design and deployment. We will provide both services and the sale of the necessary equipment to deliver the service. Cloud computing is an important element of our focus as this is an emerging market for enterprises in Queensland. Our target marketplace is medium to large corporations with complex infrastructure requirements. IT Management and above will be the typical entry point for us into these accounts. We would like to see the use of various shade of green, design should be clutter free and impress stability, trust and growth.
Updates
Hey Everyone
Just we let you all know we have changed this project to 'committed' payment status.
Looking forward to seeing the designs! Thanks for your efforts.
Best Regards
Marcus
Industry/Entity Type
Architecture
Contact Information for Business Card
Brindle Systems, Marcus Doyle, Sales Director, Level 14 Harlow Tower, 58 Penfold Street, Brisbane QLD 4000, Ph +61 7 3904 2267, M +61 4 4926 1573, E marcus.doyle@brindlesystems-example.com.au
Look and feel
Each slider illustrates characteristics of the customer's brand and the style your logo design should communicate.

```html
<!DOCTYPE html>
<html lang="en">
<head>
<meta charset="utf-8">
<title>Brindle Systems – Business Card</title>
<link rel="stylesheet" href="https://fonts.googleapis.com/css2?family=Michroma&family=Source+Sans+3:wght@400&display=swap">
<style>
  :root {
    --backdrop: #151515;
    --card-light: #eeebe9;
    --card-edge: #d7d5d3;
    --brand-green: #9fcb3d;
    --text: #2a2a2a;
    --bar: #2b2a2b;
    --bar-text: #ececec;
  }
  * { margin: 0; padding: 0; box-sizing: border-box; }
  html, body {
    width: 1200px; height: 1000px; overflow: hidden;
    background: var(--backdrop);
  }
  .card {
    position: absolute; left: 46px; top: 158px;
    width: 1110px; height: 684px;
    background: radial-gradient(ellipse at 45% 40%, var(--card-light) 0%, #e5e2e0 55%, var(--card-edge) 100%);
  }
  .brand {
    position: absolute; left: 64px; top: 106px;
    display: flex; align-items: center; gap: 20px;
  }
  .brand-mark {
    width: 44px; height: 44px;
    background: var(--brand-green);
    flex: none;
  }
  .brand-name {
    font-family: "Source Sans 3", sans-serif;
    font-weight: 400;
    font-size: 56px; line-height: 64px;
    letter-spacing: -0.5px;
    color: var(--text);
  }
  .person { position: absolute; left: 64px; top: 246px; font-family: "Source Sans 3", sans-serif; color: var(--text); }
  .person-name { font-size: 41px; line-height: 52px; letter-spacing: -0.8px; }
  .person-role { font-size: 29px; line-height: 40px; letter-spacing: -0.4px; }
  .contact-row { position: absolute; left: 27px; height: 60px; width: 700px; }
  .contact-icon {
    position: absolute; left: 0; top: 0; width: 60px; height: 60px;
    background: var(--bar);
  }
  .contact-icon svg { width: 60px; height: 60px; display: block; }
  .contact-bar {
    position: absolute; left: 71px; top: 0; width: 628px; height: 60px;
    background: var(--bar); color: var(--bar-text);
    display: flex; align-items: center;
  }
  .contact-number {
    font-family: "Michroma", sans-serif; font-size: 31px; letter-spacing: 3px;
    padding-left: 36px; -webkit-text-stroke: 0.6px var(--bar-text);
  }
  .contact-email {
    font-family: "Source Sans 3", sans-serif; font-size: 29px; letter-spacing: -0.6px;
    padding-left: 16px; white-space: nowrap;
  }
  .row-phone { top: 364px; }
  .row-mobile { top: 450px; }
  .row-email { top: 537px; }
  .address {
    position: absolute; left: 766px; top: 478px;
    font-family: "Source Sans 3", sans-serif; font-size: 29px; line-height: 45px;
    letter-spacing: -0.6px; color: var(--text); font-style: normal;
  }
</style>
</head>
<body>
  <main class="card">
    <header class="brand">
      <span class="brand-mark" aria-hidden="true"></span>
      <h1 class="brand-name">Brindle Systems</h1>
    </header>

    <div class="person">
      <p class="person-name">Marcus Doyle</p>
      <p class="person-role">Sales Director</p>
    </div>

    <div class="contact-row row-phone">
      <div class="contact-icon">
        <svg viewBox="0 0 60 60" aria-label="Phone" role="img">
          <path d="M22 14 l6 9 -4 4 q3 8 10 13 l4 -4 9 6 -3 6 q-4 3 -10 0 q-13 -8 -18 -22 q-1 -6 3 -10 z" fill="#f2f2f2"/>
        </svg>
      </div>
      <div class="contact-bar"><span class="contact-number">+61 7 3904 2267</span></div>
    </div>

    <div class="contact-row row-mobile">
      <div class="contact-icon">
        <svg viewBox="0 0 60 60" aria-label="Mobile" role="img">
          <rect x="20" y="9" width="20" height="43" rx="2" fill="#f2f2f2"/>
          <rect x="23" y="14" width="14" height="13" fill="var(--bar)"/>
          <g fill="var(--bar)">
            <rect x="23" y="31" width="3" height="3"/><rect x="28.5" y="31" width="3" height="3"/><rect x="34" y="31" width="3" height="3"/>
            <rect x="23" y="37" width="3" height="3"/><rect x="28.5" y="37" width="3" height="3"/><rect x="34" y="37" width="3" height="3"/>
            <rect x="23" y="43" width="3" height="3"/><rect x="28.5" y="43" width="3" height="3"/><rect x="34" y="43" width="3" height="3"/>
          </g>
        </svg>
      </div>
      <div class="contact-bar"><span class="contact-number">+61 4 4926 1573</span></div>
    </div>

    <div class="contact-row row-email">
      <div class="contact-icon">
        <svg viewBox="0 0 60 60" aria-label="Email" role="img">
          <rect x="9" y="18" width="42" height="26" fill="#f2f2f2"/>
          <polyline points="9,18 30,34 51,18" fill="none" stroke="var(--bar)" stroke-width="1.5"/>
          <line x1="9" y1="44" x2="25" y2="30" stroke="var(--bar)" stroke-width="1.5"/>
          <line x1="35" y1="30" x2="51" y2="44" stroke="var(--bar)" stroke-width="1.5"/>
        </svg>
      </div>
      <div class="contact-bar"><span class="contact-email">marcus.doyle@brindlesystems-example.com.au</span></div>
    </div>

    <address class="address">
      Level 14, Harlow Tower,<br>
      58 Penfold Street,<br>
      Brisbane QLD 4000
    </address>
  </main>
</body>
</html>
```